Brenton Wealth Management Flow Charts

I need help creating three flow charts for my businesses website. We want them to be simple but look professional. This is for a Wealth Management firm. I will attach a word document that has all of the descriptions for everything so you know what icons to use. We just want the chart to have an icon, the names of each step and the corresponding numbers. I will also include some examples of charts we liked as well. Once the winner is selected, we will need help with additional graphic design elements for our website ASAP.
- Goudy Roman

```html
<!DOCTYPE html>
<html lang="en">
<head>
<meta charset="utf-8">
<title>Brenton Wealth Management – Flow Charts</title>
<link rel="stylesheet" href="https://fonts.googleapis.com/css2?family=Montserrat:wght@600;700&family=Open+Sans:wght@400&family=Raleway:wght@300;400;500;600;700&display=swap">
<style>
  :root {
    --sky: #1ba3dd;
    --navy: #1e5d9a;
    --crimson: #d0245e;
    --ink: #444;
    --muted: #d9d9d9;
    --paper: #f6f6f6;
    --teal: #3bb8a8;
    --lime: #8dc63f;
    --orange: #f7941d;
    --amber: #f7a823;
    --pink: #e4166b;
    --rose: #e0245e;
    --green: #39b54a;
    --purple: #5a2a80;
    --blue: #1f63ae;
    --violet: #5b3cc4;
  }
  html, body { margin: 0; padding: 0; overflow: hidden; }
  body { background: #fff; }
  .canvas {
    position: relative;
    width: 934px;
    height: 1200px;
    overflow: hidden;
    background: radial-gradient(circle at 50% 45%, #fbfbfb 0%, var(--paper) 60%, #efefef 100%);
    font-family: "Raleway", sans-serif;
  }
  .artwork { position: absolute; inset: 0; }
  .artwork text { dominant-baseline: central; }
  .section-title { font-family: "Raleway", sans-serif; font-weight: 400; font-size: 20px; fill: var(--sky); }
  .option-tag { font-family: "Montserrat", sans-serif; font-weight: 700; font-size: 16px; fill: var(--sky); }
  .chart-title { font-family: "Montserrat", sans-serif; font-weight: 700; font-size: 11.5px; fill: var(--navy); letter-spacing: .2px; }
  .legacy-title { font-family: "Montserrat", sans-serif; font-weight: 700; font-size: 11.5px; fill: var(--crimson); }
  .step-num { font-family: "Montserrat", sans-serif; font-weight: 700; font-size: 11px; fill: var(--ink); }
  .step-num.lg { font-size: 13.5px; }
  .step-label { font-family: "Raleway", sans-serif; font-weight: 500; font-size: 8.5px; fill: var(--navy); }
  .step-label.strong { font-weight: 700; font-size: 8.8px; }
  .card-step { font-family: "Montserrat", sans-serif; font-weight: 600; font-size: 12px; }
  .pill-text { font-family: "Raleway", sans-serif; font-weight: 500; font-size: 8px; fill: #fff; }
  .ribbon-small { font-family: "Montserrat", sans-serif; font-weight: 600; font-size: 7px; fill: #fff; }
  .ribbon-big { font-family: "Montserrat", sans-serif; font-weight: 700; font-size: 17px; fill: #fff; }
  .brand-name { font-family: "Raleway", sans-serif; font-weight: 500; fill: #555; }
  .leader { stroke: #555; stroke-width: .7; fill: none; }
  .icon { fill: none; stroke: currentColor; stroke-width: 1.5; stroke-linecap: round; stroke-linejoin: round; }
  .icon .glyph { fill: currentColor; stroke: none; font-family: "Montserrat", sans-serif; font-weight: 700; font-size: 8px; text-anchor: middle; dominant-baseline: central; }

  .intro {
    position: absolute;
    width: 392px;
    margin: 0;
    font-family: "Open Sans", sans-serif;
    font-size: 5.6px;
    line-height: 9.5px;
    color: #333;
  }
  .intro--left { left: 29px; top: 934px; }
  .intro--right { left: 494px; top: 929px; }

  .brand-ring {
    position: absolute;
    left: 635px; top: 649px;
    width: 128px; height: 128px;
    border-radius: 50%;
    background: conic-gradient(#ff9800, #ffd600, #8bc34a, #00bcd4, #2196f3, #3f51b5, #9c27b0, #e91e63, #ff5722, #ff9800);
    box-shadow: 0 3px 8px rgba(0,0,0,.18);
  }
  .brand-ring__face {
    position: absolute; inset: 6px;
    border-radius: 50%;
    background: radial-gradient(circle at 50% 40%, #ffffff 0%, #f1f1f1 70%, #e4e4e4 100%);
    box-shadow: inset 0 2px 6px rgba(0,0,0,.15);
    display: flex; flex-direction: column; align-items: center; justify-content: center;
    color: #555;
    font-family: "Raleway", sans-serif; font-weight: 500;
  }
  .brand-ring__name { font-size: 15px; letter-spacing: 1.5px; }
  .brand-ring__sub { font-size: 4.2px; letter-spacing: .8px; margin-top: 2px; }
</style>
</head>
<body>
<div class="canvas">
<svg class="artwork" width="934" height="1200" viewBox="0 0 934 1200" xmlns="http://www.w3.org/2000/svg">
  <defs>
    <filter id="soft-shadow" x="-30%" y="-30%" width="160%" height="160%">
      <feDropShadow dx="0" dy="2" stdDeviation="2" flood-color="#000" flood-opacity=".22"/>
    </filter>
    <clipPath id="fan-outline">
      <path d="M316,212 C300,192 280,185 258,187 C228,189 203,199 187,215 C172,233 166,254 168,275 C170,300 181,321 201,336 C226,351 262,356 297,352 C306,350 310,341 305,330 L288,266 Z"/>
    </clipPath>
    <linearGradient id="card-pink" x1="0" y1="0" x2="0" y2="1"><stop offset="0" stop-color="#e8207f"/><stop offset="1" stop-color="#b0155c"/></linearGradient>
    <linearGradient id="card-green" x1="0" y1="0" x2="0" y2="1"><stop offset="0" stop-color="#7cc242"/><stop offset="1" stop-color="#4ea42a"/></linearGradient>
    <linearGradient id="card-purple" x1="0" y1="0" x2="0" y2="1"><stop offset="0" stop-color="#5b2d82"/><stop offset="1" stop-color="#2c1a4e"/></linearGradient>
    <linearGradient id="card-blue" x1="0" y1="0" x2="0" y2="1"><stop offset="0" stop-color="#22b4e0"/><stop offset="1" stop-color="#1b3f8f"/></linearGradient>
    <linearGradient id="card-yellow" x1="0" y1="0" x2="0" y2="1"><stop offset="0" stop-color="#f8d51c"/><stop offset="1" stop-color="#f59b10"/></linearGradient>
    <linearGradient id="card-olive" x1="0" y1="0" x2="0" y2="1"><stop offset="0" stop-color="#d4dc40"/><stop offset="1" stop-color="#a8c030"/></linearGradient>
    <linearGradient id="column-shade" x1="0" y1="0" x2="1" y2="0"><stop offset="0" stop-color="#000" stop-opacity="0"/><stop offset=".5" stop-color="#000" stop-opacity=".12"/><stop offset="1" stop-color="#000" stop-opacity="0"/></linearGradient>

    <path id="hex-outer" d="M0,-33 L28.6,-16.5 L28.6,16.5 L0,33 L-28.6,16.5 L-28.6,-16.5 Z"/>
    <path id="hex-inner" d="M0,-26 L22.5,-13 L22.5,13 L0,26 L-22.5,13 L-22.5,-13 Z"/>

    <symbol id="i-team" viewBox="0 0 24 24" class="icon">
      <circle cx="12" cy="6" r="2.2"/><circle cx="5" cy="9" r="1.8"/><circle cx="19" cy="9" r="1.8"/>
      <path d="M8,20 v-5 a4,4 0 0 1 8,0 v5"/><path d="M2,20 v-3 a3,3 0 0 1 5,-2"/><path d="M22,20 v-3 a3,3 0 0 0 -5,-2"/>
    </symbol>
    <symbol id="i-idea" viewBox="0 0 24 24" class="icon">
      <path d="M8,16 a6.5,6.5 0 1 1 8,0 v2.5 h-8 z"/><path d="M9.5,21 h5"/>
      <circle cx="12" cy="10" r="2"/><circle cx="12" cy="10" r="3.8" stroke-dasharray="1.5 1.2"/>
    </symbol>
    <symbol id="i-plan" viewBox="0 0 24 24" class="icon">
      <rect x="3" y="5" width="16" height="15"/><rect x="9" y="11" width="5" height="3"/>
      <path d="M6,19 v-3 h11 v3"/><path d="M15,10 l5,-7"/><path d="M5,8 h4"/>
    </symbol>
    <symbol id="i-gear" viewBox="0 0 24 24" class="icon">
      <circle cx="12" cy="12" r="8" stroke-width="3" stroke-dasharray="2.6 1.6"/>
      <circle cx="12" cy="12" r="5.2"/><path d="M9.6,12.2 l1.8,1.8 l3.2,-3.6"/>
    </symbol>
    <symbol id="i-merge" viewBox="0 0 24 24" class="icon">
      <path d="M11,4 v16"/><path d="M13,4 v16"/>
      <path d="M3,12 h5.5"/><path d="M6.5,9.5 l2.5,2.5 -2.5,2.5"/>
      <path d="M21,12 h-5.5"/><path d="M17.5,9.5 l-2.5,2.5 2.5,2.5"/>
    </symbol>
    <symbol id="i-thumb" viewBox="0 0 24 24" class="icon">
      <rect x="4" y="8" width="3" height="7"/>
      <path d="M7,8 l3,-5 a1.4,1.4 0 0 1 2.4,1 l-.5,3.5 h4.6 a1.4,1.4 0 0 1 1.4,1.8 l-1.4,5.7 h-9.5"/>
      <path d="M5,20 l1,-1.5 1,1.5 M11,20 l1,-1.5 1,1.5 M17,20 l1,-1.5 1,1.5"/>
    </symbol>
    <symbol id="i-growth" viewBox="0 0 24 24" class="icon">
      <path d="M3,15 l5,-5 3,2 6,-7"/><path d="M14,5 h3 v3"/>
      <circle cx="14" cy="17" r="4"/><text class="glyph" x="14" y="17.3">$</text>
    </symbol>
    <symbol id="i-coin" viewBox="0 0 24 24" class="icon">
      <circle cx="12" cy="12" r="9" stroke-dasharray="4 1.5"/><circle cx="12" cy="12" r="5.5"/>
      <text class="glyph" x="12" y="12.3">$</text>
    </symbol>
    <symbol id="i-timer" viewBox="0 0 24 24" class="icon">
      <circle cx="9" cy="13" r="6"/><path d="M9,13 v-3"/><path d="M8,5 h2"/>
      <path d="M15,20 v-4 q0,-4 3,-4 q3,0 3,4 v4 z"/><text class="glyph" x="18" y="16.8" style="font-size:5px">$</text>
    </symbol>
    <symbol id="i-network" viewBox="0 0 24 24" class="icon">
      <circle cx="12" cy="13" r="4.5"/><text class="glyph" x="12" y="13.3">$</text>
      <circle cx="5" cy="5" r="1.6"/><circle cx="19" cy="5" r="1.6"/><circle cx="4" cy="20" r="1.6"/><circle cx="20" cy="20" r="1.6"/>
      <path d="M6.2,6.2 l2.7,3.3 M17.8,6.2 l-2.7,3.3 M5.2,18.8 l3.4,-2.9 M18.8,18.8 l-3.4,-2.9"/>
    </symbol>
    <symbol id="i-present" viewBox="0 0 24 24" class="icon">
      <rect x="2" y="4" width="13" height="10"/><path d="M5,11 v-2 M8,11 v-4 M11,11 v-3"/>
      <circle cx="19" cy="6" r="1.6"/><path d="M19,8.5 v6.5 M17,20 l2,-5 2,5 M14,10 l5,1"/>
      <path d="M4,19 h2 M9,19 h2"/>
    </symbol>
    <symbol id="i-hands" viewBox="0 0 24 24" class="icon">
      <rect x="8.5" y="3" width="7" height="5"/><path d="M12,8 v4"/><path d="M10,10.5 l2,2 2,-2"/>
      <path d="M2,13 q2,6 10,7 q8,-1 10,-7"/><path d="M6,15 l4,3 M18,15 l-4,3"/>
    </symbol>
    <symbol id="i-handshake" viewBox="0 0 24 24" class="icon">
      <path d="M1,10 l4,-3 h4 l3,2"/><path d="M23,10 l-4,-3 h-5 l-5,4 a1.3,1.3 0 0 0 2,2 l2.5,-1.5 l5,4"/>
      <path d="M5,13 l3,3 M8,12 l4,4 M11,14 l3,3"/><path d="M19,15.5 l-3,2"/>
    </symbol>
    <symbol id="i-house" viewBox="0 0 24 24" class="icon">
      <path d="M4,11 l8,-7 8,7"/><path d="M6,9.5 v5 M18,9.5 v5"/>
      <text class="glyph" x="12" y="11">%</text>
      <path d="M2,17 h6 l4,2 h9"/><path d="M2,21 h10 l9,-3"/>
    </symbol>
    <symbol id="i-plant" viewBox="0 0 24 24" class="icon">
      <text class="glyph" x="12" y="4" style="font-size:7px">$</text>
      <path d="M12,15 v-6"/><path d="M12,12 q-4,0 -4,-4 q4,0 4,4"/><path d="M12,11 q4,0 4,-4 q-4,0 -4,4"/>
      <path d="M2,17 h5 q3,0 5,2 h4"/><path d="M2,21 h10 l10,-6"/>
    </symbol>
    <symbol id="i-donate" viewBox="0 0 24 24" class="icon">
      <rect x="7" y="13" width="10" height="8"/><path d="M10,13 v-1.5 h4 v1.5"/>
      <circle cx="13" cy="7" r="3"/><text class="glyph" x="13" y="7.2" style="font-size:5px">$</text>
      <path d="M3,8 q4,-5 9,-4 h6 l3,-2"/>
    </symbol>
  </defs>

  <!-- ========== Section dividers ========== -->
  <g class="dividers" stroke="#999" stroke-width=".8">
    <line x1="422" y1="80" x2="422" y2="446"/>
    <line x1="74" y1="519" x2="860" y2="519"/>
    <line x1="473" y1="539" x2="473" y2="866"/>
    <line x1="74" y1="878" x2="860" y2="878"/>
    <line x1="455" y1="888" x2="455" y2="1174"/>
  </g>

  <!-- ========== Financial Planning · Option 1 ========== -->
  <g class="financial-planning fp-radial">
    <text class="section-title" x="234" y="84" text-anchor="middle">FINANCIAL PLANNING</text>
    <text class="option-tag" x="337" y="120" text-anchor="middle">OPTION-1</text>

    <g class="fan" clip-path="url(#fan-outline)" stroke="#fff" stroke-width="1.4">
      <polygon fill="#5aa8c0" points="288,266 468,-34 132,44"/>
      <polygon fill="#3f86b5" points="288,266 132,44 -48,161"/>
      <polygon fill="#3e7db2" points="288,266 -48,161 -48,341"/>
      <polygon fill="#4b90ba" points="288,266 -48,341 99,431"/>
      <polygon fill="#539fbf" points="288,266 99,431 222,530"/>
      <polygon fill="#63b0c6" points="288,266 222,530 408,566"/>
    </g>
    <g class="fan-icons" style="color:#fff">
      <use href="#i-team" x="260" y="192" width="20" height="20"/>
      <use href="#i-idea" x="219" y="212" width="20" height="20"/>
      <use href="#i-plan" x="192" y="252" width="20" height="20"/>
      <use href="#i-gear" x="212" y="293" width="20" height="20"/>
      <use href="#i-merge" x="247" y="319" width="20" height="20"/>
    </g>
    <g class="brand-badge">
      <circle cx="292" cy="268" r="52" fill="#fff" filter="url(#soft-shadow)"/>
      <text class="brand-name" x="292" y="264" text-anchor="middle" font-size="13" letter-spacing="1.2">BRENTON</text>
      <text class="brand-name" x="292" y="277" text-anchor="middle" font-size="4.2" letter-spacing=".8">WEALTH MANAGEMENT</text>
    </g>

    <g class="leaders">
      <path class="leader" d="M270,154 H298 V190"/>
      <path class="leader" d="M186,177 H214 V206"/>
      <path class="leader" d="M136,243 H173"/>
      <path class="leader" d="M171,317 H200"/>
      <path class="leader" d="M245,362 H258 V351"/>
      <path class="leader" d="M283,393 H295 V353"/>
    </g>
    <g class="fan-labels">
      <text class="step-num" x="254" y="154" text-anchor="middle">01</text>
      <text class="step-label" x="254" y="164" text-anchor="middle">GOAL ORIENTATION</text>
      <text class="step-num" x="170" y="177" text-anchor="middle">02</text>
      <text class="step-label" x="170" y="188" text-anchor="middle">FINANCIAL REVIEW</text>
      <text class="step-num" x="125" y="243" text-anchor="middle">03</text>
      <text class="step-label" x="103" y="255">PLANNING &amp;</text>
      <text class="step-label" x="103" y="266">FORECASTING</text>
      <text class="step-num" x="159" y="317" text-anchor="middle">04</text>
      <text class="step-label" x="157" y="328" text-anchor="middle">STRATEGIC GUIDANCE</text>
      <text class="step-num" x="232" y="362" text-anchor="middle">05</text>
      <text class="step-label" x="225" y="374" text-anchor="middle">IMPLEMENTATION</text>
      <text class="step-num lg" x="273" y="393" text-anchor="middle">06</text>
      <text class="step-label" x="253" y="405" text-anchor="middle">OUR REVIEW PROCESS</text>
    </g>
  </g>

  <!-- ========== Financial Planning · Option 2 ========== -->
  <g class="financial-planning fp-timeline">
    <text class="section-title" x="621" y="84" text-anchor="middle">FINANCIAL PLANNING</text>
    <text class="option-tag" x="895" y="120" text-anchor="end">OPTION-2</text>

    <path class="wave" d="M443,274 C475,274 482,298 502,298 S546,271 566,271 S608,298 628,298 S671,271 691,271 S735,298 755,298 S797,271 817,271 S860,290 883,292" fill="none" stroke="#fff" stroke-width="9" stroke-linecap="round" filter="url(#soft-shadow)"/>

    <g class="stems" stroke="#777" stroke-width=".8">
      <line x1="502" y1="174" x2="502" y2="188"/><line x1="628" y1="174" x2="628" y2="188"/><line x1="753" y1="174" x2="753" y2="188"/>
      <line x1="502" y1="266" x2="502" y2="298"/><line x1="628" y1="266" x2="628" y2="298"/><line x1="755" y1="266" x2="755" y2="298"/>
      <line x1="566" y1="271" x2="566" y2="301"/><line x1="691" y1="271" x2="691" y2="301"/><line x1="817" y1="271" x2="817" y2="301"/>
      <line x1="566" y1="377" x2="566" y2="400"/><line x1="691" y1="377" x2="691" y2="400"/><line x1="817" y1="377" x2="817" y2="400"/>
    </g>
    <g class="wave-dots">
      <circle cx="502" cy="298" r="4" fill="#c8166b"/><circle cx="628" cy="298" r="4" fill="#6cb52d"/><circle cx="755" cy="298" r="4" fill="#5a2a7a"/>
      <circle cx="566" cy="271" r="4" fill="#1a5aa0"/><circle cx="691" cy="271" r="4" fill="#1a5aa0"/><circle cx="817" cy="271" r="4" fill="#1a5aa0"/>
    </g>

    <g class="pills">
      <rect x="459" y="161" width="84" height="13" rx="6.5" fill="#b5195e"/><text class="pill-text" x="501" y="167.5" text-anchor="middle">GOAL ORIENTATION</text>
      <rect x="586" y="161" width="83" height="13" rx="6.5" fill="#5a9a2a"/><text class="pill-text" x="627.5" y="167.5" text-anchor="middle">FINANCIAL REVIEW</text>
      <rect x="694" y="161" width="117" height="13" rx="6.5" fill="#6b3c8a"/><text class="pill-text" x="752.5" y="167.5" text-anchor="middle">PLANNING &amp; FORECASTING</text>
      <rect x="520" y="400" width="94" height="13" rx="6.5" fill="#1d4e8c"/><text class="pill-text" x="567" y="406.5" text-anchor="middle">STRATEGIC GUIDANCE</text>
      <rect x="651" y="398" width="82" height="13" rx="6.5" fill="#f08a24"/><text class="pill-text" x="692" y="404.5" text-anchor="middle">IMPLEMENTATION</text>
      <rect x="757" y="399" width="117" height="13" rx="6.5" fill="#6ab42e"/><text class="pill-text" x="815.5" y="405.5" text-anchor="middle">OUR REVIEW PROCESS</text>
    </g>

    <g class="step-card" transform="translate(468.5,188)" filter="url(#soft-shadow)">
      <path d="M0,4 Q0,0 4,0 H63 Q67,0 67,4 V20 H0 Z" fill="#fff"/>
      <path d="M0,20 H67 V64 Q67,68 63,68 H41 L33.5,78 L26,68 H4 Q0,68 0,64 Z" fill="url(#card-pink)"/>
      <text class="card-step" x="33.5" y="10.5" text-anchor="middle" fill="#d3156a">STEP-1</text>
      <use href="#i-team" x="20" y="30" width="27" height="27" style="color:#fff"/>
    </g>
    <g class="step-card" transform="translate(594.5,188)" filter="url(#soft-shadow)">
      <path d="M0,4 Q0,0 4,0 H63 Q67,0 67,4 V20 H0 Z" fill="#fff"/>
      <path d="M0,20 H67 V64 Q67,68 63,68 H41 L33.5,78 L26,68 H4 Q0,68 0,64 Z" fill="url(#card-green)"/>
      <text class="card-step" x="33.5" y="10.5" text-anchor="middle" fill="#7cbf2f">STEP-3</text>
      <use href="#i-plan" x="20" y="30" width="27" height="27" style="color:#fff"/>
    </g>
    <g class="step-card" transform="translate(721.5,188)" filter="url(#soft-shadow)">
      <path d="M0,4 Q0,0 4,0 H63 Q67,0 67,4 V20 H0 Z" fill="#fff"/>
      <path d="M0,20 H67 V64 Q67,68 63,68 H41 L33.5,78 L26,68 H4 Q0,68 0,64 Z" fill="url(#card-purple)"/>
      <text class="card-step" x="33.5" y="10.5" text-anchor="middle" fill="#4a2270">STEP-5</text>
      <use href="#i-merge" x="20" y="30" width="27" height="27" style="color:#fff"/>
    </g>

    <g class="step-card" transform="translate(532.5,301)" filter="url(#soft-shadow)">
      <path d="M4,10 H26 L33.5,0 L41,10 H63 Q67,10 67,14 V54 H0 V14 Q0,10 4,10 Z" fill="url(#card-blue)"/>
      <path d="M0,54 H67 V72 Q67,76 63,76 H4 Q0,76 0,72 Z" fill="#fff"/>
      <text class="card-step" x="33.5" y="65.5" text-anchor="middle" fill="#1d4e94">STEP-2</text>
      <use href="#i-idea" x="20" y="18" width="27" height="27" style="color:#fff"/>
    </g>
    <g class="step-card" transform="translate(657.5,301)" filter="url(#soft-shadow)">
      <path d="M4,10 H26 L33.5,0 L41,10 H63 Q67,10 67,14 V54 H0 V14 Q0,10 4,10 Z" fill="url(#card-yellow)"/>
      <path d="M0,54 H67 V72 Q67,76 63,76 H4 Q0,76 0,72 Z" fill="#fff"/>
      <text class="card-step" x="33.5" y="65.5" text-anchor="middle" fill="#f5a31a">STEP-4</text>
      <use href="#i-gear" x="20" y="18" width="27" height="27" style="color:#fff"/>
    </g>
    <g class="step-card" transform="translate(783.5,301)" filter="url(#soft-shadow)">
      <path d="M4,10 H26 L33.5,0 L41,10 H63 Q67,10 67,14 V54 H0 V14 Q0,10 4,10 Z" fill="url(#card-olive)"/>
      <path d="M0,54 H67 V72 Q67,76 63,76 H4 Q0,76 0,72 Z" fill="#fff"/>
      <text class="card-step" x="33.5" y="65.5" text-anchor="middle" fill="#b7c434">STEP-6</text>
      <use href="#i-thumb" x="20" y="18" width="27" height="27" style="color:#fff"/>
    </g>
  </g>

  <!-- ========== Investment Management · Option 1 ========== -->
  <g class="investment hex-chain">
    <text class="option-tag" x="384" y="549" text-anchor="middle">OPTION-1</text>
    <text class="chart-title" x="90" y="574">COMPREHENSIVE INVESTMENT MANAGEMENT</text>

    <polyline points="71,731 115,683 181,760 237,683 305,760 360,683 404,713" fill="none" stroke="#a8a8a8" stroke-width="1.2"/>

    <g class="hex" transform="translate(71,731)" style="color:var(--teal)">
      <use href="#hex-outer" fill="#fff" stroke="currentColor" stroke-width="3.5" filter="url(#soft-shadow)"/>
      <use href="#hex-inner" fill="#f3f3f3" stroke="#e2e2e2" stroke-width=".8"/>
      <use href="#i-idea" x="-11" y="-11" width="22" height="22"/>
    </g>
    <g class="hex" transform="translate(138,713)" style="color:var(--lime)">
      <use href="#hex-outer" fill="#fff" stroke="currentColor" stroke-width="3.5" filter="url(#soft-shadow)"/>
      <use href="#hex-inner" fill="#f3f3f3" stroke="#e2e2e2" stroke-width=".8"/>
      <use href="#i-growth" x="-11" y="-11" width="22" height="22"/>
    </g>
    <g class="hex" transform="translate(204,731)" style="color:var(--orange)">
      <use href="#hex-outer" fill="#fff" stroke="currentColor" stroke-width="3.5" filter="url(#soft-shadow)"/>
      <use href="#hex-inner" fill="#f3f3f3" stroke="#e2e2e2" stroke-width=".8"/>
      <use href="#i-coin" x="-11" y="-11" width="22" height="22"/>
    </g>
    <g class="hex" transform="translate(270,713)" style="color:#e9457a">
      <use href="#hex-outer" fill="#fff" stroke="currentColor" stroke-width="3.5" filter="url(#soft-shadow)"/>
      <use href="#hex-inner" fill="#f3f3f3" stroke="#e2e2e2" stroke-width=".8"/>
      <use href="#i-timer" x="-11" y="-11" width="22" height="22"/>
    </g>
    <g class="hex" transform="translate(338,731)" style="color:var(--amber)">
      <use href="#hex-outer" fill="#fff" stroke="currentColor" stroke-width="3.5" filter="url(#soft-shadow)"/>
      <use href="#hex-inner" fill="#f3f3f3" stroke="#e2e2e2" stroke-width=".8"/>
      <use href="#i-network" x="-11" y="-11" width="22" height="22"/>
    </g>
    <g class="hex" transform="translate(404,713)" style="color:var(--green)">
      <use href="#hex-outer" fill="#fff" stroke="currentColor" stroke-width="3.5" filter="url(#soft-shadow)"/>
      <use href="#hex-inner" fill="#f3f3f3" stroke="#e2e2e2" stroke-width=".8"/>
      <use href="#i-present" x="-11" y="-11" width="22" height="22"/>
    </g>

    <g class="leaders">
      <path class="leader" d="M58,657 H85 M71,660 V698"/>
      <path class="leader" d="M190,622 H218 M204,640 V698"/>
      <path class="leader" d="M338,672 V698"/>
      <path class="leader" d="M138,746 V789 M124,791 H151"/>
      <path class="leader" d="M270,746 V767 M257,783 H283"/>
      <path class="leader" d="M404,746 V790"/>
    </g>
    <g class="hex-labels">
      <text class="step-num lg" x="71" y="648" text-anchor="middle">01</text>
      <text class="step-num lg" x="204" y="613" text-anchor="middle">03</text>
      <text class="step-label" x="198" y="632" text-anchor="middle" style="fill:var(--orange)">ASSET ALLOCATION</text>
      <text class="step-num lg" x="338" y="648" text-anchor="middle">05</text>
      <text class="step-label" x="342" y="664" text-anchor="middle" style="fill:var(--orange)">DISTRIBUTION STRATEGY</text>
      <text class="step-num lg" x="138" y="801" text-anchor="middle">02</text>
      <text class="step-label" x="136" y="818" text-anchor="middle" style="fill:var(--lime)">INVESTMENT DECISIONS</text>
      <text class="step-num lg" x="270" y="775" text-anchor="middle">04</text>
      <text class="step-label" x="269" y="791" text-anchor="middle" style="fill:var(--rose)">TAX MITIGATION</text>
      <text class="step-num lg" x="403" y="800" text-anchor="middle" style="fill:var(--green)">06</text>
      <text class="step-label" x="394" y="818" text-anchor="middle" style="fill:var(--green)">BEHAVIORAL FINANCE COACHING</text>
    </g>
  </g>

  <!-- ========== Investment Management · Option 2 ========== -->
  <g class="investment hub">
    <text class="option-tag" x="864" y="557" text-anchor="end">OPTION-2</text>
    <text class="chart-title" x="690" y="592" text-anchor="middle">COMPREHENSIVE INVESTMENT MANAGEMENT</text>

    <g class="satellite" transform="translate(605,643)" style="color:var(--orange)">
      <circle r="22" fill="#fff" filter="url(#soft-shadow)"/>
      <circle r="20" fill="none" stroke="currentColor" stroke-width="1" stroke-dasharray="2.5 2"/>
      <circle r="22.5" fill="none" stroke="currentColor" stroke-width="2.5" stroke-dasharray="50 200" transform="rotate(-20)"/>
      <use href="#i-idea" x="-10" y="-10" width="20" height="20"/>
    </g>
    <g class="satellite" transform="translate(581,711)" style="color:#e8195c">
      <circle r="22" fill="#fff" filter="url(#soft-shadow)"/>
      <circle r="20" fill="none" stroke="currentColor" stroke-width="1" stroke-dasharray="2.5 2"/>
      <circle r="22.5" fill="none" stroke="currentColor" stroke-width="2.5" stroke-dasharray="50 200" transform="rotate(-50)"/>
      <use href="#i-growth" x="-10" y="-10" width="20" height="20"/>
    </g>
    <g class="satellite" transform="translate(602,777)" style="color:#a349c8">
      <circle r="22" fill="#fff" filter="url(#soft-shadow)"/>
      <circle r="20" fill="none" stroke="currentColor" stroke-width="1" stroke-dasharray="2.5 2"/>
      <circle r="22.5" fill="none" stroke="currentColor" stroke-width="2.5" stroke-dasharray="50 200" transform="rotate(-70)"/>
      <use href="#i-coin" x="-10" y="-10" width="20" height="20"/>
    </g>
    <g class="satellite" transform="translate(792,643)" style="color:#ef3e5c">
      <circle r="22" fill="#fff" filter="url(#soft-shadow)"/>
      <circle r="20" fill="none" stroke="currentColor" stroke-width="1" stroke-dasharray="2.5 2"/>
      <circle r="22.5" fill="none" stroke="currentColor" stroke-width="2.5" stroke-dasharray="50 200" transform="rotate(-150)"/>
      <use href="#i-timer" x="-10" y="-10" width="20" height="20"/>
    </g>
    <g class="satellite" transform="translate(817,711)" style="color:#f58a1f">
      <circle r="22" fill="#fff" filter="url(#soft-shadow)"/>
      <circle r="20" fill="none" stroke="#2aa8e0" stroke-width="1" stroke-dasharray="2.5 2"/>
      <circle r="22.5" fill="none" stroke="#2aa8e0" stroke-width="2.5" stroke-dasharray="50 200" transform="rotate(100)"/>
      <use href="#i-network" x="-10" y="-10" width="20" height="20"/>
    </g>
    <g class="satellite" transform="translate(796,777)" style="color:var(--green)">
      <circle r="22" fill="#fff" filter="url(#soft-shadow)"/>
      <circle r="20" fill="none" stroke="var(--violet)" stroke-width="1" stroke-dasharray="2.5 2"/>
      <circle r="22.5" fill="none" stroke="var(--violet)" stroke-width="2.5" stroke-dasharray="50 200" transform="rotate(120)"/>
      <use href="#i-present" x="-10" y="-10" width="20" height="20"/>
    </g>

    <g class="pointers">
      <polygon points="630,650 650,648 641,664" fill="#f7941d"/>
      <polygon points="611,701 629,711 611,721" fill="#e8195c"/>
      <polygon points="630,771 649,759 642,779" fill="#c72fd6"/>
      <polygon points="768,650 748,648 757,664" fill="#7ed957"/>
      <polygon points="788,703 770,713 788,723" fill="#1ba3e8"/>
      <polygon points="768,772 749,759 756,779" fill="#3f3fd6"/>
    </g>

    <g class="hub-labels">
      <text class="step-num lg" x="515" y="660">01</text>
      <text class="step-label" x="515" y="675" style="fill:#2ab89a">RISK TOLERANCE ASSESSMENT</text>
      <text class="step-num lg" x="524" y="727">02</text>
      <text class="step-label" x="526" y="740" style="fill:var(--rose)">INVESTMENT DECISIONS</text>
      <text class="step-num lg" x="549" y="794">03</text>
      <text class="step-label" x="549" y="808" style="fill:var(--orange)">ASSET ALLOCATION</text>
      <text class="step-num lg" x="847" y="660" text-anchor="end">04</text>
      <text class="step-label" x="847" y="674" text-anchor="end" style="fill:var(--rose)">TAX MITIGATION</text>
      <text class="step-num lg" x="889" y="729" text-anchor="end">05</text>
      <text class="step-label" x="891" y="740" text-anchor="end" style="fill:var(--orange)">DISTRIBUTION STRATEGY</text>
      <text class="step-num lg" x="878" y="798" text-anchor="end">06</text>
      <text class="step-label" x="879" y="812" text-anchor="end" style="fill:var(--green)">BEHAVIORAL FINANCE COACHING</text>
    </g>
  </g>

  <!-- ========== Legacy & Estate · Option 1 ========== -->
  <g class="legacy legacy-columns">
    <text class="legacy-title" x="226" y="917" text-anchor="middle">LEGACY AND ESTATE PLANNING</text>
    <text class="option-tag" x="379" y="923" text-anchor="middle">OPTION-1</text>

    <g class="column-shades" fill="url(#column-shade)">
      <rect x="90" y="985" width="5" height="137"/><rect x="177" y="985" width="5" height="137"/>
      <rect x="264" y="985" width="5" height="137"/><rect x="351" y="985" width="5" height="137"/>
      <rect x="437" y="985" width="5" height="137"/>
    </g>

    <g class="medallions" style="color:#fff">
      <circle cx="52" cy="1012" r="27" fill="var(--amber)"/><use href="#i-hands" x="38" y="998" width="28" height="28"/>
      <circle cx="136" cy="1012" r="27" fill="var(--blue)"/><use href="#i-handshake" x="122" y="998" width="28" height="28"/>
      <circle cx="220" cy="1012" r="27" fill="var(--purple)"/><use href="#i-house" x="206" y="998" width="28" height="28"/>
      <circle cx="310" cy="1012" r="27" fill="#7ab833"/><use href="#i-plant" x="296" y="998" width="28" height="28"/>
      <circle cx="393" cy="1012" r="27" fill="var(--pink)"/><use href="#i-donate" x="379" y="998" width="28" height="28"/>
    </g>
    <g class="leaders">
      <path class="leader" d="M52,1040 V1053 M40,1067 H64"/>
      <path class="leader" d="M136,1040 V1053 M124,1067 H148"/>
      <path class="leader" d="M220,1040 V1053 M208,1067 H232"/>
      <path class="leader" d="M310,1040 V1053 M298,1067 H322"/>
      <path class="leader" d="M393,1040 V1053 M381,1067 H405"/>
    </g>
    <g class="column-labels">
      <text class="step-num" x="51" y="1060" text-anchor="middle" style="fill:var(--amber)">01</text>
      <text class="step-label strong" x="48" y="1076" text-anchor="middle" style="fill:var(--amber)">BENEFICIARIES</text>
      <text class="step-num" x="134" y="1060" text-anchor="middle" style="fill:var(--blue)">02</text>
      <text class="step-label strong" x="134" y="1076" text-anchor="middle" style="fill:var(--blue)">TRUSTS</text>
      <text class="step-num" x="220" y="1060" text-anchor="middle" style="fill:var(--purple)">03</text>
      <text class="step-label" x="219" y="1078" text-anchor="middle" style="fill:#3a3a5a">ASSESSMENT OF</text>
      <text class="step-label" x="219" y="1089" text-anchor="middle" style="fill:#3a3a5a">ESTATE &amp; TAXES</text>
      <text class="step-num" x="308" y="1060" text-anchor="middle" style="fill:#7ab833">04</text>
      <text class="step-label strong" x="310" y="1076" text-anchor="middle" style="fill:#7ab833">ANNUAL GIVING</text>
      <text class="step-num" x="392" y="1060" text-anchor="middle" style="fill:var(--pink)">05</text>
      <text class="step-label" x="393" y="1078" text-anchor="middle" style="fill:var(--pink)">CHARITABLE</text>
      <text class="step-label" x="393" y="1088" text-anchor="middle" style="fill:var(--pink)">CONTRIBUTIONS</text>
    </g>
  </g>

  <!-- ========== Legacy & Estate · Option 2 ========== -->
  <g class="legacy legacy-ribbons">
    <text class="legacy-title" x="690" y="917" text-anchor="middle">LEGACY AND ESTATE PLANNING</text>
    <text class="option-tag" x="852" y="916" text-anchor="middle">OPTION-2</text>

    <g class="column-shades" fill="url(#column-shade)">
      <rect x="496" y="982" width="5" height="135"/><rect x="582" y="955" width="5" height="135"/>
      <rect x="661" y="1010" width="5" height="130"/><rect x="742" y="985" width="5" height="130"/>
      <rect x="828" y="955" width="5" height="135"/>
    </g>

    <g class="ribbon" transform="translate(478,1011)">
      <polygon points="0,30 10,30 10,38" fill="#a3200f"/>
      <path d="M0,0 H55 Q65,0 65,10 V30 H0 Z" fill="#f03a24"/>
      <text class="ribbon-small" x="6" y="15.5">STEP</text><text class="ribbon-big" x="27" y="15">01</text>
    </g>
    <g class="ribbon" transform="translate(565,982)">
      <polygon points="0,30 10,30 10,38" fill="#0f5585"/>
      <path d="M0,0 H55 Q65,0 65,10 V30 H0 Z" fill="#1b87c9"/>
      <text class="ribbon-small" x="6" y="15.5">STEP</text><text class="ribbon-big" x="27" y="15">02</text>
    </g>
    <g class="ribbon" transform="translate(643,1037)">
      <polygon points="0,30 10,30 10,38" fill="#0d6b7c"/>
      <path d="M0,0 H55 Q65,0 65,10 V30 H0 Z" fill="#1aa0b8"/>
      <text class="ribbon-small" x="6" y="15.5">STEP</text><text class="ribbon-big" x="27" y="15">03</text>
    </g>
    <g class="ribbon" transform="translate(726,1011)">
      <polygon points="0,30 10,30 10,38" fill="#4e7d1c"/>
      <path d="M0,0 H55 Q65,0 65,10 V30 H0 Z" fill="#7ab833"/>
      <text class="ribbon-small" x="6" y="15.5">STEP</text><text class="ribbon-big" x="27" y="15">04</text>
    </g>
    <g class="ribbon" transform="translate(811,982)">
      <polygon points="0,30 10,30 10,38" fill="#b8760a"/>
      <path d="M0,0 H55 Q65,0 65,10 V30 H0 Z" fill="#f7a823"/>
      <text class="ribbon-small" x="6" y="15.5">STEP</text><text class="ribbon-big" x="27" y="15">05</text>
    </g>

    <g class="ribbon-icons">
      <g style="color:#f03a24"><circle cx="517" cy="1070" r="16" fill="#fff" stroke="currentColor" stroke-width="2.5"/><use href="#i-hands" x="506" y="1059" width="22" height="22"/></g>
      <g style="color:#1b87c9"><circle cx="604" cy="1048" r="16" fill="#fff" stroke="currentColor" stroke-width="2.5"/><use href="#i-handshake" x="593" y="1037" width="22" height="22"/></g>
      <g style="color:#1aa0b8"><circle cx="683" cy="1092" r="16" fill="#fff" stroke="currentColor" stroke-width="2.5"/><use href="#i-house" x="672" y="1081" width="22" height="22"/></g>
      <g style="color:#7ab833"><circle cx="768" cy="1071" r="16" fill="#fff" stroke="currentColor" stroke-width="2.5"/><use href="#i-plant" x="757" y="1060" width="22" height="22"/></g>
      <g style="color:#f7a823"><circle cx="853" cy="1048" r="16" fill="#fff" stroke="currentColor" stroke-width="2.5"/><use href="#i-donate" x="842" y="1037" width="22" height="22"/></g>
    </g>
    <g class="ribbon-labels">
      <text class="step-label strong" x="532" y="1106" text-anchor="middle" style="fill:#f03a24">BENEFICIARIES</text>
      <text class="step-label strong" x="606" y="1087" text-anchor="middle" style="fill:#1f4e8c">TRUSTS</text>
      <text class="step-label" x="665" y="1126" style="fill:#1a8fa6">ASSESSMENT OF</text>
      <text class="step-label" x="665" y="1136" style="fill:#1a8fa6">ESTATE &amp; TAXES</text>
      <text class="step-label strong" x="778" y="1106" text-anchor="middle" style="fill:#7ab833">ANNUAL GIVING</text>
      <text class="step-label" x="832" y="1087" style="fill:var(--pink)">CHARITABLE</text>
      <text class="step-label" x="832" y="1097" style="fill:var(--pink)">CONTRIBUTIONS</text>
    </g>
  </g>
</svg>

<div class="brand-ring">
  <div class="brand-ring__face">
    <span class="brand-ring__name">BRENTON</span>
    <span class="brand-ring__sub">WEALTH MANAGEMENT</span>
  </div>
</div>

<p class="intro intro--left">At Brenton Wealth Management we are dedicated to protecting and preserving what you have saved for your legacy. You have put in the time, energy and effort your whole life to build your estate. We are dedicated to ensuring that you leave a legacy that will be around well beyond your time. We will have safeguards in place to make certain that your heirs are taken care of or to make sure the funds are distributed to those you deem in need. We have the planning tools and will implement customized strategies to make certain you have an impact on your future generations.</p>
<p class="intro intro--right">At Brenton Wealth Management we are dedicated to protecting and preserving what you have saved for your legacy. You have put in the time, energy and effort your whole life to build your estate. We are dedicated to ensuring that you leave a legacy that will be around well beyond your time. We will have safeguards in place to make certain that your heirs are taken care of or to make sure the funds are distributed to those you deem in need. We have the planning tools and will implement customized strategies to make certain you have an impact on your future generations.</p>
</div>
</body>
</html>
```